Civic Holdwell Business Card

We are looking to design new business cards for our company. We have two office locations and would like to have both full addresses on the card. Each address needs two lines for the building name and street address and a line or two for the city, state and zip code. There should be a place for 2-3 phone numbers. The addresses and phone numbers are at the bottom of this description. We also need a place to put our company website and one email address. Our logo is attached.
We would like the card to be two sided. The back of the card should have a blue background with some part of our logo design on it. We would like the full logo on the front of the card as well. The front of the card should have a white background with the blue logo. We are open to listing our addresses on the front or the back of the card. The person who designed our logo gave us an excellent business card idea that we really liked. I have attached a picture of his business card idea so that we can build off of it.
Addresses:
The Tanner Hall
2184 17th Street NW
Washington, DC 20007
Marlow Crest Tower
410 Dorsen Avenue #2215
Miami, FL 33131
Phone Numbers: (202) 555-0148
(202) 555-0193
Website: www.civicholdwell.example

```html
<!DOCTYPE html>
<html lang="en">
<head>
<meta charset="utf-8">
<title>Civic Holdwell Business Card</title>
<link rel="stylesheet" href="https://fonts.googleapis.com/css2?family=Lato:wght@300;400;700&display=swap">
<style>
  :root {
    --navy: #263f8c;
    --royal: #2f50c6;
    --ink: #2a3f91;
    --paper: #ffffff;
    --backdrop: #e9e9ec;
    --white-soft: rgba(255,255,255,0.92);
  }
  * { box-sizing: border-box; margin: 0; padding: 0; }
  html, body {
    width: 1200px; height: 1000px; overflow: hidden;
    background: var(--backdrop);
    font-family: "Lato", sans-serif;
  }
  .sheet { position: relative; width: 1200px; height: 1000px; }
  .card {
    position: absolute; left: 250px; width: 700px; height: 400px;
    border-radius: 34px; overflow: hidden;
    box-shadow: 0 6px 18px rgba(0,0,0,0.18);
  }
  /* Back side */
  .card-back { top: 60px; background: var(--navy); }
  .back-band {
    position: absolute; left: 70px; top: 0; width: 210px; height: 220px;
    background: var(--royal);
    border-bottom-left-radius: 40px;
  }
  .back-details {
    position: absolute; left: 60px; right: 80px; top: 234px;
    color: var(--paper);
  }
  .address-primary {
    font-weight: 700; font-size: 21px; line-height: 1.15; letter-spacing: 0.2px;
  }
  .address-secondary {
    font-weight: 300; font-size: 20px; line-height: 1.15; color: var(--white-soft);
  }
  .rule {
    border: 0; border-top: 2px dotted rgba(255,255,255,0.85);
    margin: 7px 0 6px;
  }
  .website { font-weight: 400; font-size: 20px; }
  /* Front side */
  .card-front { top: 540px; background: var(--paper); }
  .brand {
    position: absolute; left: 60px; top: 80px;
    display: flex; align-items: center; gap: 20px;
  }
  .brand-square {
    width: 84px; height: 84px; background: var(--ink); border-radius: 8px;
  }
  .brand-name {
    color: var(--ink); font-weight: 300; font-size: 52px;
    letter-spacing: 4px; text-transform: uppercase; white-space: nowrap;
  }
  .contact {
    position: absolute; left: 260px; right: 60px; bottom: 70px;
    color: var(--ink); font-size: 22px; font-weight: 400;
    white-space: nowrap;
  }
  .contact .rule { border-top-color: var(--ink); margin: 8px 0 10px; }
  .phones { display: flex; align-items: center; gap: 10px; }
  .phone-icon { width: 20px; height: 20px; fill: var(--ink); flex: none; }
</style>
</head>
<body>
<main class="sheet">
  <section class="card card-back" aria-label="Card back">
    <div class="back-band"></div>
    <div class="back-details">
      <p class="address-primary">The Tanner Hall, 2184 17th Street NW,<br>Washington, DC 20007</p>
      <hr class="rule">
      <p class="address-secondary">Marlow Crest Tower, 410 Dorsen Avenue #2215<br>Miami, FL 33131</p>
      <hr class="rule">
      <p class="website">www.civicholdwell.example</p>
    </div>
  </section>

  <section class="card card-front" aria-label="Card front">
    <div class="brand">
      <span class="brand-square"></span>
      <span class="brand-name">Civic Holdwell</span>
    </div>
    <div class="contact">
      <p class="email">info@civicholdwell.example</p>
      <hr class="rule">
      <p class="phones">
        <svg class="phone-icon" viewBox="0 0 24 24" aria-hidden="true">
          <path d="M6.6 10.8a15.1 15.1 0 0 0 6.6 6.6l2.2-2.2a1 1 0 0 1 1-.25 11.4 11.4 0 0 0 3.6.57 1 1 0 0 1 1 1V20a1 1 0 0 1-1 1A17 17 0 0 1 3 4a1 1 0 0 1 1-1h3.5a1 1 0 0 1 1 1c0 1.25.2 2.45.57 3.57a1 1 0 0 1-.25 1z"/>
        </svg>
        <span>(202) 555-0148 &nbsp;|&nbsp; (202) 555-0193</span>
      </p>
    </div>
  </section>
</main>
</body>
</html>
```